Photobook template design

Just one book of 4/5 pages needed to find a handful of designers to help with this project that will be ongoing for several months, we will agree design price per book.

Hi there, we need lots of fabulous photobook templates designed:
there will be 20 books to start with, canvas layouts, calendar layouts etc.

The MAIN idea of the template is to facilitate the easiest creation / ordering of photobooks etc. possible for the client, so all they have to do is upload their pics and drop them into the templates you're going to design...

Each photobook needs to have min 20 pages, there can be a common theme throughout, but they must be different enough so that they do not all blend into one.
Choose to create a design from the following categories:
family
kids
travel
romance / love
seasonal holiday
year in review
everyday / general
recipes
pets / animals
collage
scrapbook

the quality and look and feel must be equal to www.pagerivo.example / www.snapduvel.example / www.framelyst.example.uk

In order to keep the designs as fresh as possible - we will work with several designers, so for this first project we will choose 1 designer, but then we'll create other design projects for which you will be specifically invited to design for - it's the only way the do multiple designs/projects.

please see 2 pics attached of other templates already designed - we're very happy with these...

Target Market(s)

These photobooks / calendars / canvas prints are for the average family - not too serious, must be fun / tongue in cheek etc.
They're for people who want to do photobooks but have no clue or do not have the time - so they must LOVE the design, and then want to just add their photos...

Industry/Entity Type

Travel

Requirements
Must have
• Must be designed in Indesign or Illustrator.
Metric sizes please - Either A3 landscape or portrait with 3 mm bleed, or 300 x 300mm square - 3mm bleed
If you place photos for proofing, please use imagorra images - we have a imagorra account

```html
<!DOCTYPE html>
<html lang="en">
<head>
<meta charset="utf-8">
<title>Romance Photobook – Template Spreads</title>
<link rel="stylesheet" href="https://fonts.googleapis.com/css2?family=Great+Vibes&family=Dancing+Script:wght@500&display=swap">
<style>
  :root {
    --canvas: #ffffff;
    --wine-deep: #3a0306;
    --wine: #6e0a0f;
    --crimson: #a8121a;
    --scarlet: #d21f26;
    --gold-light: #f6e3a4;
    --gold: #d8b25a;
    --gold-dark: #9c7424;
    --paper: #fbfbf9;
    --caption: #c4162a;
    --ribbon-red: #c8141c;
  }
  * { box-sizing: border-box; }
  html, body {
    margin: 0;
    width: 1200px;
    height: 855px;
    overflow: hidden;
    background: var(--canvas);
  }
  .sheet { position: relative; width: 1200px; height: 855px; }

  .spread {
    position: absolute;
    width: 560px;
    height: 396px;
    overflow: hidden;
    background:
      radial-gradient(circle at 30% 25%, rgba(255,80,80,.35) 0, transparent 38%),
      radial-gradient(circle at 75% 60%, rgba(230,40,40,.3) 0, transparent 35%),
      linear-gradient(180deg, var(--crimson) 0%, var(--wine) 45%, var(--wine-deep) 62%, var(--wine) 80%, var(--crimson) 100%);
  }
  .spread--one   { left: 22px;  top: 22px; }
  .spread--two   { left: 617px; top: 22px; }
  .spread--three { left: 22px;  top: 443px; }
  .spread--four  { left: 617px; top: 443px; }

  .ribbons { position: absolute; inset: 0; width: 560px; height: 396px; }

  .album-name {
    position: absolute;
    margin: 0;
    padding: 4px 14px 8px;
    font-family: "Great Vibes", cursive;
    font-weight: 400;
    font-size: 60px;
    line-height: 1;
    white-space: nowrap;
    color: var(--gold);
    background: linear-gradient(180deg, var(--gold-light), var(--gold) 55%, var(--gold-dark));
    -webkit-background-clip: text;
    background-clip: text;
    -webkit-text-fill-color: transparent;
    z-index: 3;
  }

  .print {
    position: absolute;
    margin: 0;
    background: var(--paper);
    padding: 7px 7px 0;
    box-shadow: 2px 4px 10px rgba(0,0,0,.45);
    z-index: 1;
  }
  .print__photo { width: 100%; }
  .print__caption {
    margin: 0;
    font-family: "Dancing Script", cursive;
    font-weight: 500;
    color: var(--caption);
    line-height: 1;
    padding-left: 12px;
    white-space: nowrap;
  }

  .photo--beach-hug   { background: linear-gradient(180deg, #8fbbe6 0%, #d7e6f2 40%, #b07a5c 70%, #7c4b34 100%); }
  .photo--sunset-sand { background: linear-gradient(180deg, #e9b47c 0%, #b7a48c 40%, #6d8a8a 55%, #b39a7a 75%, #8a6d52 100%); }
  .photo--wedding-kiss{ background: linear-gradient(135deg, #5a3a22 0%, #d7b48a 45%, #f3eee6 70%, #8a6a52 100%); }
  .photo--rose-scent  { background: linear-gradient(120deg, #3f5a3a 0%, #6f8c5a 35%, #d9c6b0 55%, #c8a22a 100%); }
  .photo--sunlit-vows { background: linear-gradient(160deg, #f7e2b0 0%, #e0b486 35%, #6a5a7c 70%, #3e3552 100%); }

  .ornament { position: absolute; z-index: 2; }
  .bow-gold {
    width: 58px; height: 50px;
    border-radius: 50%;
    background: radial-gradient(circle, var(--gold-light) 0, var(--gold) 45%, var(--gold-dark) 100%);
  }
  .bow-red {
    width: 34px; height: 30px;
    border-radius: 50%;
    background: radial-gradient(circle, #f0505a 0, var(--ribbon-red) 55%, #7a0a0e 100%);
  }
  .heart { width: 40px; height: 36px; }
  .keepsake-bottle {
    background: linear-gradient(180deg, #f3a6c8 0%, #c2306e 40%, #7a1340 100%);
    border-radius: 6px 6px 4px 4px;
  }
  .couple-figure {
    border-radius: 30px 30px 6px 6px;
    background: linear-gradient(180deg, rgba(240,228,212,.55) 0%, rgba(120,90,100,.45) 55%, rgba(40,28,36,.35) 100%);
  }
</style>
</head>
<body>
<main class="sheet">

  <section class="spread spread--one">
    <svg class="ribbons" viewBox="0 0 560 396" aria-hidden="true">
      <defs>
        <linearGradient id="gold-band-a" x1="0" y1="0" x2="0" y2="1">
          <stop offset="0" stop-color="#f6e3a4"/><stop offset=".5" stop-color="#d8b25a"/><stop offset="1" stop-color="#9c7424"/>
        </linearGradient>
      </defs>
      <rect x="14" y="0" width="10" height="396" fill="#c8141c"/>
      <polygon points="0,312 0,332 150,396 180,396" fill="url(#gold-band-a)"/>
      <polygon points="408,0 440,0 560,50 560,72" fill="url(#gold-band-a)"/>
    </svg>
    <h1 class="album-name" style="left:30px; top:4px;">Album Name</h1>

    <figure class="print" style="left:28px; top:78px; width:280px; height:285px; transform:rotate(-2deg);">
      <div class="print__photo photo--beach-hug" style="height:235px;" role="img" aria-label="Photo slot: couple embracing on a sunny beach"></div>
      <figcaption class="print__caption" style="font-size:22px; padding-top:10px; padding-left:62px;">Photo tile</figcaption>
    </figure>
    <figure class="print" style="left:346px; top:26px; width:192px; height:155px; transform:rotate(4deg);">
      <div class="print__photo photo--sunset-sand" style="height:112px;" role="img" aria-label="Photo slot: couple sitting on the sand at sunset"></div>
      <figcaption class="print__caption" style="font-size:17px; padding-top:6px;">Photo tile</figcaption>
    </figure>
    <figure class="print" style="left:350px; top:218px; width:185px; height:160px; transform:rotate(-4deg);">
      <div class="print__photo photo--wedding-kiss" style="height:118px;" role="img" aria-label="Photo slot: bride and groom kissing"></div>
      <figcaption class="print__caption" style="font-size:17px; padding-top:6px;">Photo tile</figcaption>
    </figure>

    <div class="ornament bow-gold" style="left:4px; top:312px;" role="img" aria-label="Gold ribbon bow"></div>
    <div class="ornament bow-gold" style="left:510px; top:30px;" role="img" aria-label="Gold ribbon bow"></div>
    <div class="ornament bow-red" style="left:4px; top:30px;" role="img" aria-label="Red ribbon bow"></div>
    <svg class="ornament heart" style="left:332px; top:212px;" viewBox="0 0 40 36" role="img" aria-label="Red heart"><path d="M20 34 C4 22 0 14 4 7 C8 0 17 1 20 8 C23 1 32 0 36 7 C40 14 36 22 20 34Z" fill="#d21f26"/></svg>
    <svg class="ornament heart" style="left:290px; top:328px; width:34px; height:30px;" viewBox="0 0 40 36" role="img" aria-label="Red heart"><path d="M20 34 C4 22 0 14 4 7 C8 0 17 1 20 8 C23 1 32 0 36 7 C40 14 36 22 20 34Z" fill="#d21f26"/></svg>
  </section>

  <section class="spread spread--two">
    <svg class="ribbons" viewBox="0 0 560 396" aria-hidden="true">
      <defs>
        <linearGradient id="gold-band-b" x1="0" y1="0" x2="0" y2="1">
          <stop offset="0" stop-color="#f6e3a4"/><stop offset=".5" stop-color="#d8b25a"/><stop offset="1" stop-color="#9c7424"/>
        </linearGradient>
      </defs>
      <rect x="530" y="0" width="10" height="396" fill="#c8141c"/>
      <polygon points="0,50 0,72 165,0 135,0" fill="url(#gold-band-b)"/>
      <polygon points="0,318 0,340 140,396 170,396" fill="url(#gold-band-b)"/>
    </svg>
    <h2 class="album-name" style="left:204px; top:10px;">Album Name</h2>

    <figure class="print" style="left:22px; top:25px; width:150px; height:145px; transform:rotate(-5deg);">
      <div class="print__photo photo--wedding-kiss" style="height:106px;" role="img" aria-label="Photo slot: bride and groom kissing"></div>
      <figcaption class="print__caption" style="font-size:16px; padding-top:6px;">Photo tile</figcaption>
    </figure>
    <figure class="print" style="left:28px; top:180px; width:190px; height:150px; transform:rotate(4deg);">
      <div class="print__photo photo--sunset-sand" style="height:108px;" role="img" aria-label="Photo slot: couple sitting on the sand at sunset"></div>
      <figcaption class="print__caption" style="font-size:17px; padding-top:6px;">Photo tile</figcaption>
    </figure>
    <figure class="print" style="left:271px; top:98px; width:260px; height:272px;">
      <div class="print__photo photo--rose-scent" style="height:218px;" role="img" aria-label="Photo slot: couple sharing a red rose"></div>
      <figcaption class="print__caption" style="font-size:22px; padding-top:10px; padding-left:26px;">Photo tile</figcaption>
    </figure>

    <div class="ornament bow-gold" style="left:0; top:28px;" role="img" aria-label="Gold ribbon bow"></div>
    <div class="ornament bow-gold" style="left:4px; top:316px;" role="img" aria-label="Gold ribbon bow"></div>
    <div class="ornament bow-red" style="left:518px; top:74px;" role="img" aria-label="Red ribbon bow"></div>
    <svg class="ornament heart" style="left:192px; top:166px;" viewBox="0 0 40 36" role="img" aria-label="Red hearts"><path d="M20 34 C4 22 0 14 4 7 C8 0 17 1 20 8 C23 1 32 0 36 7 C40 14 36 22 20 34Z" fill="#d21f26"/></svg>
    <div class="ornament keepsake-bottle" style="left:258px; top:273px; width:30px; height:100px;" role="img" aria-label="Pink perfume bottle with rose"></div>
  </section>

  <section class="spread spread--three">
    <svg class="ribbons" viewBox="0 0 560 396" aria-hidden="true">
      <defs>
        <linearGradient id="gold-band-c" x1="0" y1="0" x2="0" y2="1">
          <stop offset="0" stop-color="#f6e3a4"/><stop offset=".5" stop-color="#d8b25a"/><stop offset="1" stop-color="#9c7424"/>
        </linearGradient>
      </defs>
      <rect x="534" y="0" width="10" height="396" fill="#c8141c"/>
      <polygon points="0,52 0,74 160,0 130,0" fill="url(#gold-band-c)"/>
      <polygon points="0,320 0,342 140,396 170,396" fill="url(#gold-band-c)"/>
    </svg>
    <h2 class="album-name" style="left:152px; top:16px; font-size:50px;">Album Name</h2>

    <figure class="print" style="left:12px; top:72px; width:155px; height:160px; transform:rotate(-6deg);">
      <div class="print__photo photo--rose-scent" style="height:118px;" role="img" aria-label="Photo slot: couple sharing a red rose"></div>
      <figcaption class="print__caption" style="font-size:16px; padding-top:6px; padding-left:30px;">Photo tile</figcaption>
    </figure>
    <figure class="print" style="left:390px; top:40px; width:160px; height:155px; transform:rotate(6deg);">
      <div class="print__photo photo--wedding-kiss" style="height:114px;" role="img" aria-label="Photo slot: bride and groom kissing"></div>
      <figcaption class="print__caption" style="font-size:16px; padding-top:6px;">Photo tile</figcaption>
    </figure>
    <figure class="print" style="left:185px; top:183px; width:183px; height:185px;">
      <div class="print__photo photo--beach-hug" style="height:145px;" role="img" aria-label="Photo slot: couple embracing on a sunny beach"></div>
      <figcaption class="print__caption" style="font-size:16px; padding-top:8px; padding-left:44px;">Photo tile</figcaption>
    </figure>

    <div class="ornament bow-gold" style="left:0; top:30px;" role="img" aria-label="Gold ribbon bow"></div>
    <div class="ornament bow-gold" style="left:8px; top:320px;" role="img" aria-label="Gold ribbon bow"></div>
    <div class="ornament bow-gold" style="left:384px; top:46px; width:36px; height:32px;" role="img" aria-label="Small gold bow"></div>
    <div class="ornament bow-red" style="left:522px; top:200px;" role="img" aria-label="Red ribbon bow"></div>
    <svg class="ornament heart" style="left:162px; top:160px; width:54px; height:48px;" viewBox="0 0 40 36" role="img" aria-label="Red heart"><path d="M20 34 C4 22 0 14 4 7 C8 0 17 1 20 8 C23 1 32 0 36 7 C40 14 36 22 20 34Z" fill="#d21f26"/></svg>
    <svg class="ornament heart" style="left:140px; top:204px; width:34px; height:30px;" viewBox="0 0 40 36" role="img" aria-label="Red heart"><path d="M20 34 C4 22 0 14 4 7 C8 0 17 1 20 8 C23 1 32 0 36 7 C40 14 36 22 20 34Z" fill="#d21f26"/></svg>
    <svg class="ornament heart" style="left:338px; top:162px; width:56px; height:50px;" viewBox="0 0 40 36" role="img" aria-label="Red heart"><path d="M20 34 C4 22 0 14 4 7 C8 0 17 1 20 8 C23 1 32 0 36 7 C40 14 36 22 20 34Z" fill="#e23a44"/></svg>
    <div class="ornament couple-figure" style="left:356px; top:256px; width:62px; height:112px;" role="img" aria-label="Illustration area: bride and groom standing together"></div>
  </section>

  <section class="spread spread--four">
    <svg class="ribbons" viewBox="0 0 560 396" aria-hidden="true">
      <defs>
        <linearGradient id="gold-band-d" x1="0" y1="0" x2="0" y2="1">
          <stop offset="0" stop-color="#f6e3a4"/><stop offset=".5" stop-color="#d8b25a"/><stop offset="1" stop-color="#9c7424"/>
        </linearGradient>
      </defs>
      <rect x="22" y="0" width="10" height="396" fill="#c8141c"/>
      <polygon points="395,0 428,0 560,58 560,80" fill="url(#gold-band-d)"/>
      <polygon points="0,318 0,340 140,396 170,396" fill="url(#gold-band-d)"/>
    </svg>

    <figure class="print" style="left:26px; top:32px; width:215px; height:322px;">
      <div class="print__photo photo--sunlit-vows" style="height:272px;" role="img" aria-label="Photo slot: wedding couple in warm sunlight"></div>
      <figcaption class="print__caption" style="font-size:20px; padding-top:10px; padding-left:50px;">Photo tile</figcaption>
    </figure>
    <figure class="print" style="left:253px; top:19px; width:168px; height:138px; transform:rotate(-3deg);">
      <div class="print__photo photo--sunset-sand" style="height:100px;" role="img" aria-label="Photo slot: couple sitting on the sand at sunset"></div>
      <figcaption class="print__caption" style="font-size:15px; padding-top:6px;">Photo tile</figcaption>
    </figure>
    <figure class="print" style="left:413px; top:105px; width:133px; height:103px; transform:rotate(-4deg);">
      <div class="print__photo photo--wedding-kiss" style="height:72px;" role="img" aria-label="Photo slot: bride and groom kissing"></div>
      <figcaption class="print__caption" style="font-size:13px; padding-top:4px;">Photo tile</figcaption>
    </figure>
    <h2 class="album-name" style="left:248px; top:208px; font-size:56px;">Album Name</h2>

    <div class="ornament bow-red" style="left:10px; top:34px;" role="img" aria-label="Red ribbon bow"></div>
    <div class="ornament bow-gold" style="left:512px; top:34px;" role="img" aria-label="Gold ribbon bow"></div>
    <div class="ornament bow-gold" style="left:0; top:318px; width:50px; height:44px;" role="img" aria-label="Gold ribbon bow"></div>
    <svg class="ornament heart" style="left:222px; top:18px;" viewBox="0 0 40 36" role="img" aria-label="Red heart"><path d="M20 34 C4 22 0 14 4 7 C8 0 17 1 20 8 C23 1 32 0 36 7 C40 14 36 22 20 34Z" fill="#d21f26"/></svg>
    <svg class="ornament heart" style="left:350px; top:172px;" viewBox="0 0 40 36" role="img" aria-label="Red hearts"><path d="M20 34 C4 22 0 14 4 7 C8 0 17 1 20 8 C23 1 32 0 36 7 C40 14 36 22 20 34Z" fill="#d21f26"/></svg>
    <div class="ornament couple-figure" style="left:440px; top:262px; width:62px; height:114px;" role="img" aria-label="Illustration area: bride and groom seated together"></div>
  </section>

</main>
</body>
</html>
```